Website for Plumbing Company, Sir FlowBoiler

I need a 7-page fully HTML-coded website for my plumbing company, Sir FlowBoiler. We specialize in installation, repair, and replacement of both gas and electric water heaters. Although we offer both tankless (on-demand) water heaters and standard (with tank) water heaters, most of our business is related to standard (with tank) water heaters in the USA market.

These are the pages I need:
1. Home page with sections such as About Us, Our Services, Why Choose Us, Testimonials, Location Map (Palm Beach County Florida), Quote Request Form, Join Our Newsletter, Mission Statement, etc.

2. Gas Water Heaters

3. Electric Water Heaters

4. Tankless Water Heaters

5. About Us

6. Contact Us

7. Privacy Policy, Terms & Conditions

Be sure to mention the following points:
1. Same-Day Service
2. Best Price Guarantee
3. 100% Satisfaction Rating
4. 15-Year Warranty on Water Heater & Parts
5. Lifetime Warranty on Workmanship
*All Warranties are Transferrable Upon Home Sale

Once design is selected and finalized, I need the website coded in a standard HTML/CSS and temporarily hosted on your development server so I can see the website functionality that is not observable from screenshots, such as section animations, etc. Once those details are finalized, I will move the source code to my server and complete the project.

Target Market(s)

Residential Home Owners and Business Owners

Industry/Entity Type

Plumbing, Home Services, Remodeling, Construction

Coding

Coded - Design and coding required

Number of Pages Required

5+ page

Colors
0054AA
0677BA
7BADD7
CADEEF
E8F1F8
FFC000
F8CF3A
FAE287
FDF2CF
FEFAEE
EE7325
F08F49
F5BC92
FAE3D3
FDF4ED

Requirements
Must have
• Clean, colorful, and professional

```html
<!DOCTYPE html>
<html lang="en">
<head>
<meta charset="utf-8">
<title>Sir FlowBoiler — Water Heater Experts</title>
<link href="https://fonts.googleapis.com/css2?family=Fira+Sans:wght@400;500;600;700&display=swap" rel="stylesheet">
<style>
:root{
  --blue-deep:#0054AA;
  --blue:#0677BA;
  --blue-navy:#1f3f7f;
  --blue-ink:#23375f;
  --blue-soft:#7BADD7;
  --blue-pale:#CADEEF;
  --blue-mist:#E8F1F8;
  --orange:#EE7325;
  --orange-light:#F08F49;
  --orange-pale:#FAE3D3;
  --paper:#f5f3f0;
  --card:#fbfaf8;
  --line:#dcdad6;
  --text:#4a4f5c;
  --canvas:#d9dbe6;
}
*{box-sizing:border-box;margin:0;padding:0}
html,body{width:800px;height:1200px;overflow:hidden}
body{background:var(--canvas);font-family:"Fira Sans",Arial,sans-serif;color:var(--text);position:relative}
.page{position:absolute;left:146px;top:0;width:556px;height:1143px;background:var(--paper);box-shadow:0 2px 10px rgba(40,50,80,.18);overflow:hidden}
.btn{display:inline-flex;align-items:center;justify-content:center;border-radius:3px;font-weight:600;color:#fff;background:linear-gradient(var(--orange-light),var(--orange));box-shadow:0 1px 3px rgba(0,0,0,.2);white-space:nowrap}
.btn-blue{background:linear-gradient(#2f5ea8,var(--blue-navy))}

/* header */
.site-header{position:absolute;left:0;top:0;width:556px;height:46px;background:linear-gradient(var(--orange-light),var(--orange))}
.brand{position:absolute;left:14px;top:10px;display:flex;align-items:center;gap:7px}
.brand-mark{width:24px;height:24px;border-radius:50%;background:#fff;opacity:.9}
.brand-name{font-size:19px;font-weight:600;color:#fff}
.header-phone{position:absolute;left:306px;top:14px;display:flex;align-items:center;gap:5px;color:#fff;font-size:13px}
.header-quote{position:absolute;left:432px;top:11px;width:113px;height:25px;background:#f7f5f2;border-radius:3px;color:var(--blue-ink);font-size:11px;display:flex;align-items:center;justify-content:center;box-shadow:0 1px 2px rgba(0,0,0,.2)}

/* nav */
.main-nav{position:absolute;left:0;top:46px;width:556px;height:31px;background:#efeeec;display:flex;align-items:center;padding-left:36px;font-size:11px;color:var(--blue-ink)}
.main-nav a{font-weight:500}
.main-nav .sep{color:#b8b8b8;margin:0 10px}
.main-nav .muted{font-weight:400;color:#5a6275}

/* hero */
.hero{position:absolute;left:0;top:77px;width:556px;height:219px;background:linear-gradient(100deg,#2f5fa6 0%,#3e6db0 45%,#5b86bf 70%,#9fb6d2 100%)}
.hero-photo{position:absolute;left:339px;top:0;width:217px;height:219px;background:linear-gradient(160deg,#cfd6e0,#8ea3c2 55%,#3f5e92)}
.hero h1{position:absolute;left:27px;top:22px;font-size:24px;line-height:31px;font-weight:600;color:#fff;width:330px}
.hero p{position:absolute;left:27px;top:99px;font-size:14px;line-height:22px;color:#fff}
.hero .btn{position:absolute;top:159px;height:30px;font-size:12px}

/* about */
.about-card{position:absolute;left:24px;top:309px;width:506px;height:148px;background:var(--card);box-shadow:0 1px 4px rgba(0,0,0,.13)}
.about-card h2{position:absolute;left:18px;top:10px;font-size:17px;font-weight:600;color:var(--blue-ink)}
.about-lead{position:absolute;left:18px;top:38px;width:240px;font-size:10.5px;line-height:16px;color:#5a5f6a}
.about-body{position:absolute;left:18px;top:74px;width:260px;font-size:8px;line-height:14px;color:#333}
.about-card .btn{position:absolute;left:17px;top:111px;width:78px;height:21px;font-size:8.5px}
.about-rule{position:absolute;left:100px;top:122px;width:165px;height:1px;background:var(--line)}
.about-photo{position:absolute;left:284px;top:8px;width:211px;height:128px;background:linear-gradient(120deg,#e4e4e6,#b9c0cb 50%,#35508a)}

/* section titles */
.section-title{position:absolute;left:0;width:556px;display:flex;align-items:center;gap:12px;padding:0 34px;font-size:19px;font-weight:600}
.section-title::before,.section-title::after{content:"";flex:1;height:1px;background:currentColor;opacity:.3}

/* services */
.services-title{top:470px;color:var(--blue-ink)}
.service{position:absolute;top:500px;width:135px;height:132px;text-align:center}
.service+.service{border-left:1px solid var(--line)}
.service-icon{width:50px;height:44px;margin:4px auto 0;border-radius:8px;background:linear-gradient(135deg,var(--blue-soft),var(--blue-deep))}
.service-icon.alert{border-radius:50% 50% 6px 6px;background:linear-gradient(var(--orange-light),var(--orange))}
.service h3{margin-top:14px;font-size:10.5px;font-weight:600;color:var(--blue-ink)}
.service p{margin:5px auto 0;width:100px;font-size:7px;line-height:10px;color:#555}
.service .btn{margin-top:8px;width:82px;height:20px;font-size:8.5px}

/* why */
.why{position:absolute;left:0;top:645px;width:556px;height:134px;background:linear-gradient(#2f5da3,#3b66aa 60%,#3560a4)}
.why-title{top:10px;color:#fff}
.testimonial{position:absolute;left:28px;top:48px;width:502px;height:70px;background:var(--card);box-shadow:0 1px 3px rgba(0,0,0,.2)}
.avatar{position:absolute;left:14px;top:6px;width:54px;height:54px;border-radius:50%;background:linear-gradient(#c7d3e6,#2f4f8c);border:2px solid #fff}
.quote-text{position:absolute;left:99px;top:16px;width:330px;font-size:9px;line-height:14px;color:#333}
.quote-text b{font-weight:500}
.quote-mark{position:absolute;font-size:26px;color:var(--blue-pale);font-weight:700;line-height:1}
.stars{position:absolute;left:100px;top:49px;color:var(--orange);font-size:9px;letter-spacing:1px}
.author{position:absolute;left:208px;top:49px;font-size:8px;color:#333}
.author-rule{position:absolute;left:250px;top:54px;width:236px;height:1px;background:var(--line)}
.slide-arrow{position:absolute;top:69px;width:22px;height:22px;background:#f2f2f2;display:flex;align-items:center;justify-content:center;border:1px solid #ccc}

/* quote */
.quote-section h2{position:absolute;left:27px;top:791px;font-size:18px;font-weight:600;color:var(--blue-ink)}
.quote-rule{position:absolute;left:180px;top:802px;width:60px;height:1px;background:var(--line)}
.field{position:absolute;height:24px;background:#fff;border:1px solid #e3e1dd;font-size:9.5px;color:#333;padding:7px 0 0 10px}
.field.message{height:37px}
.field .chev{position:absolute;right:9px;top:7px}
.quote-section .btn{position:absolute;left:27px;top:950px;width:205px;height:33px;font-size:15px}
.map{position:absolute;left:253px;top:795px;width:280px;height:195px;background:linear-gradient(120deg,#9dc0a0 0%,#b9cfa8 40%,#7fb07c 60%,#7aa7d6 85%)}

/* newsletter */
.newsletter{position:absolute;left:0;top:1009px;width:556px;height:90px;background:linear-gradient(#3f68a8,#2f5a9d)}
.newsletter h2{position:absolute;left:88px;top:16px;font-size:17px;font-weight:600;color:#fff;display:flex;align-items:baseline;gap:9px}
.newsletter h2 span{font-size:11px;font-weight:400}
.email-input{position:absolute;left:92px;top:48px;width:267px;height:27px;background:#fff;font-size:10.5px;color:#9a9a9a;padding:7px 0 0 13px}
.newsletter .btn{position:absolute;left:365px;top:48px;width:97px;height:27px;font-size:12px}

/* footer */
.site-footer{position:absolute;left:0;top:1099px;width:556px;height:44px;background:var(--blue-navy);display:flex;align-items:center;padding-left:34px;font-size:8.5px;color:#fff;gap:6px}
.site-footer .div{opacity:.6}
.site-footer nav{display:flex;gap:6px;margin-left:14px}
</style>
</head>
<body>
<div class="page">

  <header class="site-header">
    <div class="brand"><span class="brand-mark"></span><span class="brand-name">Sir FlowBoiler</span></div>
    <div class="header-phone">
      <svg width="13" height="13" viewBox="0 0 24 24"><path fill="#fff" d="M6.6 10.8a15 15 0 006.6 6.6l2.2-2.2c.3-.3.7-.4 1-.2 1.1.4 2.3.6 3.6.6.6 0 1 .4 1 1V20c0 .6-.4 1-1 1A17 17 0 013 4c0-.6.4-1 1-1h3.5c.6 0 1 .4 1 1 0 1.3.2 2.5.6 3.6.1.3 0 .7-.2 1z"/></svg>
      (561) 555-0142
    </div>
    <a class="header-quote">Request a Quote</a>
  </header>

  <nav class="main-nav">
    <a>Home</a><span class="sep">/</span><a class="muted">About Us</a><span class="sep">/</span><a>Services</a><span class="sep">/</span><a>Contact Us</a>
  </nav>

  <section class="hero">
    <div class="hero-photo" role="img" aria-label="Smiling plumber holding a pipe wrench beside a water heater"></div>
    <h1>Palm Beach County’s Trusted Water Heater Experts</h1>
    <p>Installation, Repair &amp; Replacement<br>of Gas, Electric, &amp; Tankless Water Heaters</p>
    <a class="btn" style="left:27px;width:133px">Request a Quote</a>
    <a class="btn btn-blue" style="left:168px;width:95px">Call Now</a>
  </section>

  <section class="about-card">
    <h2>About Sir FlowBoiler</h2>
    <p class="about-lead">Your local experts in water heater installation, repair, and replacement throughout Palm Beach</p>
    <p class="about-body">We offer reliable, same day service for both residential and commercial customers. Licensed &amp; Insured. Satisfaction guaranteed!</p>
    <span class="about-rule"></span>
    <a class="btn">Learn More ›</a>
    <div class="about-photo" role="img" aria-label="Technician standing next to an installed tank water heater"></div>
  </section>

  <h2 class="section-title services-title">Our Services</h2>
  <article class="service" style="left:11px">
    <div class="service-icon" role="img" aria-label="Gas water heater unit"></div>
    <h3>Gas Water Heaters</h3>
    <p>Installation &amp; repair of reliable gas water heaters.</p>
    <a class="btn">Learn More ›</a>
  </article>
  <article class="service" style="left:146px">
    <div class="service-icon" role="img" aria-label="Electric water heater unit"></div>
    <h3>Electric Water Heaters</h3>
    <p>Service &amp; repair for efficient electric water heaters.</p>
    <a class="btn" style="width:86px">Learn More ›</a>
  </article>
  <article class="service" style="left:281px">
    <div class="service-icon" role="img" aria-label="Tankless water heater unit"></div>
    <h3>Tankless Water Heaters</h3>
    <p>Modern, on-demand tankless heating solutions.</p>
    <a class="btn" style="width:86px">Learn More ›</a>
  </article>
  <article class="service" style="left:416px">
    <div class="service-icon alert" role="img" aria-label="Emergency alarm light"></div>
    <h3>Emergency Replacement</h3>
    <p>24/7 emergency replacement whenever you need it.</p>
    <a class="btn" style="width:91px">Learn More ›</a>
  </article>

  <section class="why">
    <h2 class="section-title why-title">Why Choose Us</h2>
    <span class="slide-arrow" style="left:16px"><svg width="8" height="10" viewBox="0 0 8 10"><path d="M6 1L2 5l4 4" stroke="#777" fill="none" stroke-width="1.4"/></svg></span>
    <span class="slide-arrow" style="left:518px"><svg width="8" height="10" viewBox="0 0 8 10"><path d="M2 1l4 4-4 4" stroke="#777" fill="none" stroke-width="1.4"/></svg></span>
    <blockquote class="testimonial">
      <div class="avatar" role="img" aria-label="Customer portrait"></div>
      <span class="quote-mark" style="left:76px;top:10px">“</span>
      <p class="quote-text">Quick and reliable service! My water heater was replaced the same day. <b>Highly recommend!</b></p>
      <span class="quote-mark" style="left:426px;top:10px">”</span>
      <span class="stars">★★★★★</span>
      <span class="author">Maria K.</span>
      <span class="author-rule"></span>
    </blockquote>
  </section>

  <section class="quote-section">
    <h2>Get a Free Quote</h2>
    <span class="quote-rule"></span>
    <div class="field" style="left:25px;top:820px;width:106px">Name</div>
    <div class="field" style="left:134px;top:820px;width:106px">Phone</div>
    <div class="field" style="left:25px;top:849px;width:215px">Email</div>
    <div class="field" style="left:25px;top:878px;width:215px">Service Needed
      <svg class="chev" width="9" height="6" viewBox="0 0 9 6"><path d="M1 1l3.5 3.5L8 1" stroke="#555" fill="none" stroke-width="1.3"/></svg></div>
    <div class="field message" style="left:25px;top:907px;width:215px">Message</div>
    <a class="btn">Get a Free Quote</a>
    <div class="map" role="img" aria-label="Map of Palm Beach County, Florida service area"></div>
  </section>

  <section class="newsletter">
    <h2>Join Our Newsletter <span>Sign up for plumbing tips &amp; special offers</span></h2>
    <div class="email-input">Enter your email</div>
    <a class="btn">Subscribe</a>
  </section>

  <footer class="site-footer">
    <span>Licensed &amp; Insured</span><span class="div">|</span>
    <span>Call Us: <b>(561) 555-0187</b></span>
    <nav><a>Home</a>·<a>About Us</a>·<a>Services</a>·<a>Contact Us</a>·<a>Privacy &amp; Terms</a></nav>
  </footer>

</div>
</body>
</html>
```